Design for social media advertising campaign

Multiple designs to be produced for a legal services advertising campaign in Australia offering assistance to small to medium sized businesses facing financial issues arising from the economic consequences of Covid-19. Designs must be sized suitably for LinkedIn, Twitter and Facebook. See our website recovery.harbourline.example and Facebook page KellowayLaw.CoastCounsel for logo, colours etc. Examples of the messaging is in the 5 uploaded files.

Target Market(s)

Small / medium size business owners

Industry/Entity Type

Legal

Requirements
Must have
• Sizing for Facebook, LinkedIn and Twitter

```html
<!DOCTYPE html>
<html lang="en">
<head>
<meta charset="utf-8">
<title>Kelloway Law – Social Media Ad Set</title>
<link rel="stylesheet" href="https://fonts.googleapis.com/css2?family=Poppins:wght@300;400&family=Open+Sans:wght@400&display=swap">
<style>
  :root {
    --board: #000000;
    --label: #ffffff;
    --maroon: #5c0b11;
    --maroon-deep: #4e080d;
    --gold: #c8a44a;
    --gold-light: #e6d59e;
    --cream: #fbf8ef;
    --sky-top: #a9c6ea;
    --sky-glass: #3f63a3;
    --glass-dark: #1c2f5c;
    --white: #ffffff;
  }
  * { box-sizing: border-box; margin: 0; padding: 0; }
  html, body {
    width: 725px; height: 1200px; overflow: hidden;
    background: var(--board);
  }
  .board { position: relative; width: 725px; height: 1200px; }
  .platform-label {
    position: absolute; left: 0; width: 725px; text-align: center;
    color: var(--label);
    font-family: "Open Sans", sans-serif; font-size: 18px;
  }
  .ad { position: absolute; overflow: hidden; }
  .ad svg.ad-art { position: absolute; inset: 0; }
  .ad-line {
    position: absolute; white-space: nowrap;
    font-family: "Poppins", sans-serif; font-weight: 300;
    color: var(--white); line-height: 1;
  }
  .ad-line.is-accent { color: var(--gold); font-weight: 400; }
  .ad-footer {
    position: absolute; white-space: nowrap; line-height: 1;
    font-family: "Poppins", sans-serif; color: var(--maroon);
  }
  .ad-footer .firm { font-weight: 400; }
  .ad-footer .tagline { font-weight: 300; }
  .brand-name {
    font-family: "Poppins", sans-serif; font-weight: 400; fill: var(--maroon);
  }

  /* Facebook */
  .ad--facebook { left: 47px; top: 67px; width: 630px; height: 240px; }
  .ad--facebook .ad-line { left: 40px; font-size: 22px; }
  .ad--facebook .ad-line.is-accent { font-size: 27px; }
  .ad--facebook .ad-footer { left: 40px; top: 207px; }
  .ad--facebook .firm { font-size: 22px; }
  .ad--facebook .tagline { font-size: 17px; }

  /* LinkedIn */
  .ad--linkedin { left: 148px; top: 382px; width: 425px; height: 260px; }
  .ad--linkedin .ad-line { left: 25px; font-size: 19px; }
  .ad--linkedin .ad-line.is-accent { font-size: 25px; }
  .ad--linkedin .ad-footer { left: 25px; top: 233px; }
  .ad--linkedin .firm { font-size: 17px; }
  .ad--linkedin .tagline { font-size: 14px; }

  /* Twitter */
  .ad--twitter { left: 94px; top: 711px; width: 536px; height: 416px; }
  .ad--twitter .ad-line { left: 33px; font-size: 26px; }
  .ad--twitter .ad-line.is-accent { font-size: 34px; }
  .ad--twitter .ad-footer { left: 33px; top: 370px; }
  .ad--twitter .firm { font-size: 23px; }
  .ad--twitter .tagline { font-size: 18px; }
</style>
</head>
<body>
<main class="board">

  <!-- Facebook -->
  <p class="platform-label" style="top:30px">Facebook</p>
  <section class="ad ad--facebook">
    <svg class="ad-art" width="630" height="240" viewBox="0 0 630 240">
      <defs>
        <linearGradient id="fb-band" x1="0" x2="1" y1="0" y2="0">
          <stop offset="0" stop-color="var(--gold)"/>
          <stop offset="0.55" stop-color="var(--gold-light)"/>
          <stop offset="1" stop-color="var(--cream)"/>
        </linearGradient>
        <linearGradient id="fb-photo" x1="0" x2="0" y1="0" y2="1">
          <stop offset="0" stop-color="var(--sky-top)"/>
          <stop offset="0.45" stop-color="var(--sky-glass)"/>
          <stop offset="1" stop-color="var(--glass-dark)"/>
        </linearGradient>
      </defs>
      <rect width="630" height="240" fill="var(--cream)"/>
      <path d="M0 0 H598 Q622 90 600 170 Q585 230 560 240 H0 Z" fill="var(--maroon)"/>
      <path d="M0 240 V222 Q0 197 35 197 H300 Q380 200 460 240 Z" fill="url(#fb-band)"/>
      <path d="M0 240 V222 Q0 197 35 197 H630 V240 Z" fill="url(#fb-band)"/>
      <circle cx="506" cy="121" r="117" fill="var(--maroon)"/>
      <circle cx="506" cy="121" r="110" fill="url(#fb-photo)" role="img" aria-label="Photo: glass office tower seen from below against a blue sky"/>
      <circle cx="340" cy="107" r="46" fill="var(--white)"/>
      <text class="brand-name" x="340" y="104" font-size="12" text-anchor="middle">Kelloway</text>
      <text class="brand-name" x="340" y="119" font-size="12" text-anchor="middle">Law</text>
    </svg>
    <p class="ad-line" style="top:35px">Facing business</p>
    <p class="ad-line is-accent" style="top:63px">solvency issues?</p>
    <p class="ad-line" style="top:100px">Obtain our free</p>
    <p class="ad-line" style="top:128px">guide now.</p>
    <p class="ad-footer"><span class="firm">Kelloway Law</span> <span class="tagline">(Specialist Lawyers)</span></p>
  </section>

  <!-- LinkedIn -->
  <p class="platform-label" style="top:345px">LinkedIn</p>
  <section class="ad ad--linkedin">
    <svg class="ad-art" width="425" height="260" viewBox="0 0 425 260">
      <defs>
        <linearGradient id="li-band" x1="0" x2="1" y1="0" y2="0">
          <stop offset="0" stop-color="var(--gold)"/>
          <stop offset="0.55" stop-color="var(--gold-light)"/>
          <stop offset="1" stop-color="var(--cream)"/>
        </linearGradient>
        <linearGradient id="li-photo" x1="0" x2="0" y1="0" y2="1">
          <stop offset="0" stop-color="var(--sky-top)"/>
          <stop offset="0.45" stop-color="var(--sky-glass)"/>
          <stop offset="1" stop-color="var(--glass-dark)"/>
        </linearGradient>
      </defs>
      <rect width="425" height="260" fill="var(--cream)"/>
      <path d="M0 0 H400 Q370 30 405 110 Q430 190 390 260 H0 Z" fill="var(--maroon)"/>
      <path d="M0 260 V232 Q0 212 30 212 H425 V260 Z" fill="url(#li-band)"/>
      <circle cx="328" cy="156" r="97" fill="var(--maroon)"/>
      <circle cx="328" cy="156" r="90" fill="url(#li-photo)" role="img" aria-label="Photo: glass office tower seen from below against a blue sky"/>
      <circle cx="192" cy="144" r="38" fill="var(--white)"/>
      <text class="brand-name" x="192" y="142" font-size="10" text-anchor="middle">Kelloway</text>
      <text class="brand-name" x="192" y="155" font-size="10" text-anchor="middle">Law</text>
    </svg>
    <p class="ad-line" style="top:33px">Facing business</p>
    <p class="ad-line is-accent" style="top:56px">solvency</p>
    <p class="ad-line is-accent" style="top:83px">issues?</p>
    <p class="ad-line" style="top:112px">Obtain our</p>
    <p class="ad-line" style="top:138px">free guide</p>
    <p class="ad-line" style="top:162px">now.</p>
    <p class="ad-footer"><span class="firm">Kelloway Law</span> <span class="tagline">(Specialist Lawyers)</span></p>
  </section>

  <!-- Twitter -->
  <p class="platform-label" style="top:675px">Twitter</p>
  <section class="ad ad--twitter">
    <svg class="ad-art" width="536" height="416" viewBox="0 0 536 416">
      <defs>
        <linearGradient id="tw-band" x1="0" x2="1" y1="0" y2="0">
          <stop offset="0" stop-color="var(--gold)"/>
          <stop offset="0.55" stop-color="var(--gold-light)"/>
          <stop offset="1" stop-color="var(--cream)"/>
        </linearGradient>
        <linearGradient id="tw-photo" x1="0" x2="0" y1="0" y2="1">
          <stop offset="0" stop-color="var(--sky-top)"/>
          <stop offset="0.45" stop-color="var(--sky-glass)"/>
          <stop offset="1" stop-color="var(--glass-dark)"/>
        </linearGradient>
      </defs>
      <rect width="536" height="416" fill="var(--cream)"/>
      <path d="M0 0 H506 Q485 60 515 170 Q540 290 490 416 H0 Z" fill="var(--maroon)"/>
      <path d="M0 416 V375 Q0 345 40 345 H536 V416 Z" fill="url(#tw-band)"/>
      <circle cx="385" cy="258" r="128" fill="var(--maroon)"/>
      <circle cx="385" cy="258" r="120" fill="url(#tw-photo)" role="img" aria-label="Photo: glass office tower seen from below against a blue sky"/>
      <circle cx="204" cy="239" r="52" fill="var(--white)"/>
      <text class="brand-name" x="204" y="236" font-size="13" text-anchor="middle">Kelloway</text>
      <text class="brand-name" x="204" y="253" font-size="13" text-anchor="middle">Law</text>
    </svg>
    <p class="ad-line" style="top:47px">Facing business</p>
    <p class="ad-line is-accent" style="top:77px">solvency issues?</p>
    <p class="ad-line" style="top:117px">Obtain our</p>
    <p class="ad-line" style="top:151px">free guide</p>
    <p class="ad-line" style="top:184px">now.</p>
    <p class="ad-footer"><span class="firm">Kelloway Law</span> <span class="tagline">(Specialist Lawyers)</span></p>
  </section>

</main>
</body>
</html>
```